We need a card design for our company Pebble Harbor Services. Our goal is to save people money on their disposal services. For this post card please put our logo in it. Please use these colors Pantone 576c and 418c or green and grey. We are giving you as the designer the opportunity to be creative with any other images. We are looking to have a fun eye catching postcard.
Please write:
Think you are stuck with your trash bill? Think again
We cut your neighbors disposal cost by 40%.

Please put down our information also,
Contact us
800.555.0147
marlene@gravelnook.com
gravelnook.com

```html
<!DOCTYPE html>
<html lang="en">
<head>
<meta charset="utf-8">
<title>Pebble Harbor Services – Postcard</title>
<link rel="stylesheet" href="https://fonts.googleapis.com/css2?family=Schoolbell&family=Open+Sans:wght@400;600&display=swap">
<style>
  :root {
    --backdrop: #e0e0e0;
    --kraft-light: #c9a56c;
    --kraft-mid: #b89258;
    --kraft-dark: #a98449;
    --chalk: #ffffff;
    --brand-green: #5e9732;
    --brand-grey: #5c6058;
  }
  html, body {
    margin: 0;
    padding: 0;
    width: 1200px;
    height: 900px;
    overflow: hidden;
    background: var(--backdrop);
  }
  .postcard {
    position: absolute;
    left: 32px;
    top: 72px;
    width: 1136px;
    height: 756px;
  }
  .kraft-paper {
    position: absolute;
    inset: 0;
    background: radial-gradient(ellipse at 45% 40%, var(--kraft-light) 0%, var(--kraft-mid) 60%, var(--kraft-dark) 100%);
  }
  .chalk-frame {
    position: absolute;
    inset: 0;
  }
  .headline {
    position: absolute;
    left: 0;
    width: 1090px;
    text-align: center;
    font-family: "Schoolbell", cursive;
    color: var(--chalk);
    margin: 0;
    font-weight: 400;
  }
  .headline-line { font-size: 37px; line-height: 1; }
  .line-stuck { top: 166px; }
  .line-again { top: 222px; }
  .line-neighbors { top: 280px; }
  .line-by { top: 334px; font-size: 34px; }
  .savings-figure {
    top: 372px;
    font-size: 96px;
    line-height: 1;
    letter-spacing: 2px;
  }
  .brand {
    position: absolute;
    left: 84px;
    top: 610px;
    display: flex;
    align-items: center;
    gap: 14px;
  }
  .brand-mark {
    width: 34px;
    height: 34px;
    background: var(--brand-grey);
  }
  .brand-name {
    font-family: "Open Sans", sans-serif;
    font-weight: 600;
    font-size: 30px;
    color: var(--brand-green);
    white-space: nowrap;
  }
  .contact {
    position: absolute;
    left: 780px;
    top: 566px;
    font-family: "Open Sans", sans-serif;
    font-size: 22px;
    line-height: 32px;
    color: var(--chalk);
    margin: 0;
    font-style: normal;
  }
</style>
</head>
<body>
  <section class="postcard">
    <div class="kraft-paper" role="img" aria-label="Crumpled brown kraft paper background"></div>

    <svg class="chalk-frame" width="1136" height="756" viewBox="0 0 1136 756" aria-hidden="true">
      <g fill="none" stroke="var(--chalk)" stroke-linecap="round">
        <path d="M38 42 L1098 36 L1100 712 L40 714 Z" stroke-width="3"/>
        <path d="M44 46 L1092 44 L1094 706 L46 708 Z" stroke-width="1.5" opacity="0.8"/>
      </g>
    </svg>

    <p class="headline headline-line line-stuck">Think you are stuck with your trash bill?</p>
    <p class="headline headline-line line-again">Think again</p>
    <p class="headline headline-line line-neighbors">We cut your neighbors disposal cost</p>
    <p class="headline headline-line line-by">by</p>
    <p class="headline savings-figure">40%</p>

    <div class="brand">
      <span class="brand-mark"></span>
      <span class="brand-name">Pebble Harbor Services</span>
    </div>

    <address class="contact">
      Contact us<br>
      800.555.0147<br>
      marlene@gravelnook.com<br>
      gravelnook.com
    </address>
  </section>
</body>
</html>
```